Restaurant needs promotional material

We need a design for a "free welcome cocktail on your next visit" flyer. The flyer must have a black background and be contemporary. Our logo is the name of the restaurant which is "Amber Nook" in edwardian script font with italic selected.

There must be a section for terms and conditions, which are:
1 free cocktail for every main course ordered from our evening menu over the value of 9.95€ (not including taxes). The number of free cocktails cannot exceed the number of main courses ordered from your previous visit. This offer is only valid when you present both this flyer and your receipt from your previous visit. This offer does not include ice cream cocktails. This offer cannot be used in conjunction with any other offer or promotion. Limit 1 free cocktail per person. We reserve the right to final interpretation of this offer and can cancel the offer at any time.

A space must also be left where we can write a "valid until" date.

The uploaded photos are a picture of our cocktail menu and the publicity we are currently running, so you can get a feel for your design.

Thanks

Industry/Entity Type

Restaurant

Colors
000000

Requirements
Must have
• Also included in the flyer is the text " Please present this flyer along with your bill from your previous visit upon arrival.
• Pictures of cocktails!

```html
<!DOCTYPE html>
<html lang="en">
<head>
<meta charset="utf-8">
<title>Amber Nook — Free Welcome Cocktail Flyer</title>
<link rel="stylesheet" href="https://fonts.googleapis.com/css2?family=Great+Vibes&family=Roboto+Condensed:ital,wght@0,400;0,700;1,400;1,700&family=Oswald:wght@500;700&display=swap">
<style>
  :root {
    --ink: #000000;
    --paper: #ffffff;
    --magenta: #e21adf;
    --magenta-deep: #b10fb8;
    --violet-glow: #5a1473;
    --badge: #8c2aa3;
    --badge-edge: #c255d8;
    --curtain: #7a0a16;
    --curtain-dark: #2a0308;
    --drink-warm: #f29a2a;
    --drink-pink: #f0607a;
  }
  * { margin: 0; padding: 0; box-sizing: border-box; }
  html, body { width: 851px; height: 1200px; overflow: hidden; background: var(--ink); }
  .flyer {
    position: relative;
    width: 851px;
    height: 1200px;
    overflow: hidden;
    background:
      radial-gradient(ellipse 70% 28% at 50% 10%, var(--violet-glow) 0%, rgba(90,20,115,0.35) 45%, transparent 75%),
      var(--ink);
    color: var(--paper);
    font-family: "Roboto Condensed", "Arial Narrow", sans-serif;
  }
  .brand {
    position: absolute;
    top: 34px;
    left: 0;
    width: 100%;
    text-align: center;
  }
  .brand__kicker {
    display: block;
    font-family: "Oswald", sans-serif;
    font-weight: 700;
    font-size: 44px;
    letter-spacing: 3px;
    line-height: 1;
    margin-left: 130px;
  }
  .brand__name {
    display: block;
    font-family: "Great Vibes", cursive;
    font-size: 150px;
    line-height: 1;
    margin-top: -14px;
  }
  .hero-photo {
    position: absolute;
    top: 262px;
    left: 0;
    width: 851px;
    height: 480px;
    background:
      radial-gradient(ellipse 18% 30% at 16% 62%, var(--drink-warm) 0%, transparent 70%),
      radial-gradient(ellipse 16% 28% at 38% 58%, var(--drink-pink) 0%, transparent 70%),
      radial-gradient(ellipse 16% 22% at 60% 48%, rgba(255,255,255,0.55) 0%, transparent 70%),
      radial-gradient(ellipse 14% 22% at 82% 40%, rgba(240,220,170,0.5) 0%, transparent 70%),
      linear-gradient(180deg, var(--curtain-dark) 0%, var(--curtain) 45%, var(--curtain-dark) 100%);
    -webkit-mask-image: linear-gradient(180deg, transparent 0%, #000 14%, #000 82%, transparent 100%);
            mask-image: linear-gradient(180deg, transparent 0%, #000 14%, #000 82%, transparent 100%);
  }
  .notice {
    position: absolute;
    top: 200px;
    left: -20px;
    width: 900px;
    height: 84px;
    background: var(--magenta);
    transform: rotate(-2.6deg);
    display: flex;
    align-items: center;
    justify-content: center;
    text-align: center;
  }
  .notice__text {
    font-style: italic;
    font-size: 29px;
    line-height: 1.05;
    letter-spacing: 0.5px;
    text-transform: uppercase;
    color: var(--paper);
  }
  .offer-badge {
    position: absolute;
    top: 530px;
    left: 530px;
    width: 280px;
    height: 280px;
    border-radius: 50%;
    background: radial-gradient(circle at 40% 35%, var(--badge-edge) 0%, var(--badge) 55%, var(--magenta-deep) 100%);
    opacity: 0.92;
    display: flex;
    flex-direction: column;
    align-items: center;
    justify-content: center;
    text-align: center;
  }
  .offer-badge__free {
    font-family: "Oswald", sans-serif;
    font-weight: 500;
    font-size: 82px;
    line-height: 0.95;
    letter-spacing: 2px;
  }
  .offer-badge__line {
    font-family: "Oswald", sans-serif;
    font-weight: 500;
    font-size: 24px;
    letter-spacing: 1px;
    line-height: 1.4;
  }
  .terms {
    position: absolute;
    top: 762px;
    left: 24px;
    width: 805px;
  }
  .terms__title {
    font-weight: 400;
    font-size: 30px;
    color: var(--magenta);
    text-transform: uppercase;
    letter-spacing: 0.5px;
    margin-bottom: 14px;
  }
  .terms__body {
    font-size: 22.5px;
    line-height: 1.68;
  }
  .terms__dot { color: var(--magenta); margin: 0 6px; }
  .validity {
    position: absolute;
    top: 1148px;
    left: 545px;
    font-size: 32px;
    color: var(--magenta);
    text-transform: uppercase;
  }
</style>
</head>
<body>
<main class="flyer">
  <header class="brand">
    <span class="brand__kicker">RESTAURANT</span>
    <span class="brand__name">Amber Nook</span>
  </header>

  <div class="hero-photo" role="img" aria-label="Photograph of four colourful cocktails in glasses in front of a red curtain"></div>

  <div class="notice">
    <p class="notice__text">Please present this flyer along with your bill from<br>your previous visit upon arrival</p>
  </div>

  <div class="offer-badge">
    <span class="offer-badge__free">FREE</span>
    <span class="offer-badge__line">WELCOME COCKTAIL</span>
    <span class="offer-badge__line">ON YOUR NEXT VISIT</span>
  </div>

  <section class="terms">
    <h2 class="terms__title">Terms and conditions:</h2>
    <p class="terms__body">
      Free cocktail for every main course ordered from our evening menu over the menu over the value of 9.95€ (not including taxes)<span class="terms__dot">●</span>The number of free cocktails cannot exceed the number of main courses ordered from your previous visit.<span class="terms__dot">●</span>This offer does not include ice cream cocktails.<span class="terms__dot">●</span>This offer cannot be used in conjunction with any other offer or promotion.<span class="terms__dot">●</span>Limit 1 free cocktail per person.<span class="terms__dot">●</span>
      We reserve the right to final interpretation of this offer and can cancel the offer at any time.
    </p>
  </section>

  <p class="validity">Valid until:</p>
</main>
</body>
</html>
```